German Headhunter/ HR Consultancy needs Business Cards Design

We need a business Card Design for our Company in Stuttgart. We are specialized as Headhunter/ HR Consultancy in Placement of specialist and managers in permanent employment. Please refer to our business logo.

```html
<!DOCTYPE html>
<html lang="de">
<head>
<meta charset="utf-8">
<title>Kernfeld Personalberatung – Visitenkarte</title>
<link href="https://fonts.googleapis.com/css2?family=Montserrat:wght@500;600;700&display=swap" rel="stylesheet">
<style>
  :root {
    --page-bg: #f1f4f6;
    --card-white: #ffffff;
    --brand-blue: #3b55a5;
    --brand-grey: #959595;
    --band-light: #f0f3f5;
    --band-line: #d7dde3;
    --text-light: #ffffff;
  }
  * { margin: 0; padding: 0; box-sizing: border-box; }
  html, body {
    width: 1042px;
    height: 1200px;
    overflow: hidden;
    background: var(--page-bg);
    font-family: "Montserrat", Arial, sans-serif;
  }
  .card {
    position: absolute;
    left: 240px;
    width: 543px;
    height: 332px;
    overflow: hidden;
  }
  .card-front { top: 238px; background: var(--card-white); }
  .card-back { top: 655px; background: var(--brand-blue); }

  .brand {
    position: absolute;
    left: 41px;
    top: 118px;
    display: flex;
    align-items: center;
    gap: 16px;
    color: var(--brand-blue);
    font-weight: 600;
  }
  .brand-square {
    width: 46px;
    height: 46px;
    background: var(--brand-blue);
  }
  .brand-name { line-height: 1; }
  .brand-name .primary { display: block; font-size: 40px; letter-spacing: 1px; }
  .brand-name .secondary { display: block; font-size: 17.5px; letter-spacing: 0.6px; margin-top: 6px; }

  .contact {
    position: absolute;
    left: 41px;
    top: 94px;
    color: var(--text-light);
    font-weight: 500;
  }
  .contact-title {
    font-size: 17.5px;
    font-weight: 700;
    letter-spacing: 0.5px;
    margin-bottom: 8px;
  }
  .contact-title .accent { color: var(--brand-grey); }
  .contact p { font-size: 16px; line-height: 20.5px; }
  .contact .address { margin-bottom: 6px; }
  .contact .phones { margin-bottom: 7px; }
  .contact .label {
    display: inline-block;
    width: 18px;
    color: var(--brand-grey);
  }
  .web-band {
    position: absolute;
    left: 0;
    bottom: 0;
    width: 100%;
    height: 66px;
    background: var(--band-light);
    border: 1px solid var(--band-line);
    border-top: none;
  }
  .web-band .web {
    position: absolute;
    left: 38px;
    top: 19px;
    font-size: 21px;
    font-weight: 500;
    color: var(--brand-blue);
  }
</style>
</head>
<body>
  <section class="card card-front">
    <div class="brand">
      <div class="brand-square"></div>
      <div class="brand-name">
        <span class="primary">KERNFELD</span>
        <span class="secondary">PERSONALBERATUNG</span>
      </div>
    </div>
  </section>

  <section class="card card-back">
    <div class="contact">
      <h1 class="contact-title">KERNFELD <span class="accent">PERSONALBERATUNG</span></h1>
      <div class="address">
        <p>Lindenhofstraße 14</p>
        <p>D-70173 Stuttgart</p>
      </div>
      <div class="phones">
        <p><span class="label">T</span>+49 (0) 711 48 20 316 - 0</p>
        <p><span class="label">F</span>+49 (0) 711 48 20 316 - 49</p>
      </div>
      <p class="email">info@kernfeld.de</p>
    </div>
    <div class="web-band">
      <span class="web">www.kernfeld.de</span>
    </div>
  </section>
</body>
</html>
```